BPH Business Card 2018

Brellmore Chiropractic. We have two locations that we want to advertise on the same card. Calderwick OrthoAxis campus address: 3815 Pemberly Dr., Suite 240, Flowood, MS 39587. Madison address: 426 Larkmoor Dr., Building D., Madison, MS 39674. website: www.drbrellmore.example. o:(601)555-0148 f:(601)555-0173

Target Market(s)

Health care decision makers: primary care doctors and mothers

Contact Information for Business Card

I have no idea; up for any suggestions and I'd do much better picking from examples versus describing what I'm looking for. We are in a very high end location and would like the cards to look really sharp.

Requirements
Must have
• My name, Tobias R Venmark, D.C.

```html
<!DOCTYPE html>
<html lang="en">
<head>
<meta charset="utf-8">
<title>Brellmore Chiropractic Business Card</title>
<link href="https://fonts.googleapis.com/css2?family=Open+Sans:wght@700&family=PT+Sans:wght@400&display=swap" rel="stylesheet">
<style>
  :root {
    --backdrop: #2b2b2b;
    --card-black: #050505;
    --card-white: #f1f1f1;
    --ink-light: #ffffff;
    --ink-soft: #e6e6e6;
    --ink-dark: #2a2a2a;
    --ink-muted: #8a8a8a;
  }
  * { margin: 0; padding: 0; box-sizing: border-box; }
  html, body { width: 1200px; height: 960px; overflow: hidden; }
  body { background: var(--backdrop); position: relative; font-family: "PT Sans", Arial, sans-serif; }

  .card { position: absolute; width: 600px; height: 344px; overflow: hidden; box-shadow: 0 4px 14px rgba(0,0,0,0.55); }
  .card-front { left: 322px; top: 108px; background: var(--card-white); }
  .card-back { left: 320px; top: 492px; height: 343px; background: var(--card-black); }

  .front-panel { position: absolute; inset: 0; }

  .contact { position: absolute; left: 27px; top: 130px; color: var(--ink-soft); font-size: 14.5px; line-height: 19.5px; }
  .contact-name { font-family: "Open Sans", Arial, sans-serif; font-weight: 700; font-size: 18px; color: var(--ink-light); margin-bottom: 6px; letter-spacing: -0.2px; }
  .contact-block { margin-bottom: 5px; }

  .brand { position: absolute; left: 318px; top: 70px; display: flex; align-items: center; gap: 10px; }
  .brand-dot { width: 12px; height: 12px; border-radius: 50%; background: var(--ink-dark); }
  .brand-name { font-size: 20px; color: var(--ink-dark); letter-spacing: 1.5px; text-transform: uppercase; }

  .back-brand { position: absolute; left: 0; right: 0; top: 140px; text-align: center; color: var(--ink-muted); font-size: 22px; letter-spacing: 3px; text-transform: uppercase; }
  .back-web { position: absolute; left: 0; right: 0; top: 281px; text-align: center; color: var(--ink-soft); font-size: 14px; letter-spacing: 4px; text-transform: uppercase; }
</style>
</head>
<body>
  <section class="card card-front">
    <svg class="front-panel" width="600" height="344" viewBox="0 0 600 344" aria-hidden="true">
      <polygon points="0,0 194,0 392,344 0,344" fill="var(--card-black)"/>
      <line x1="186" y1="0" x2="372" y2="344" stroke="var(--ink-light)" stroke-width="2"/>
    </svg>

    <div class="brand">
      <span class="brand-dot"></span>
      <span class="brand-name">Brellmore Chiropractic</span>
    </div>

    <div class="contact">
      <p class="contact-name">TOBIAS R VENMARK, D.C.</p>
      <p class="contact-block">Calderwick OrthoAxis campus :<br>3815 Pemberly Dr., Suite 240<br>Flowood, MS 39587.</p>
      <p class="contact-block">Madison address:<br>426 Larkmoor Dr., Building D.<br>Madison, MS 39674.</p>
      <p>P. (601)555-0148F. (601)555-0173<br>W. www.drbrellmore.example</p>
    </div>
  </section>

  <section class="card card-back">
    <p class="back-brand">Brellmore Chiropractic</p>
    <p class="back-web">www.drbrellmore.example</p>
  </section>
</body>
</html>
```